Criminal Defense Lawyer needs business cards and stationary
Dunmore Law Office
Criminal Defense Lawyer needs business cards and stationary - Law
Creative Brief
Simple
Ray Dunmore
418 N Willowbend Ave Lincoln, IL 62871
ray@dunmorelawoffice.example
dunmorelawoffice.example
I would like a simple/modern design for the front side of my card. I am thinking simply my logo in white with a blue background (same blue as in my logo). Other background colors to be considered are black and gray. That said, please be creative, I am open to any cutting edge design as long as it is not busy.
On the reverse side I would like my contact information displayed to include: My Name (Ray Dunmore) Dunmore Law Office (optional depending on design of front of card) Phone: 217-555-0143 email: ray@dunmorelawoffice.example Website: DunmoreLawOffice.example I do not want my address included. I am looking to create a visually modern yet simple design that is not too busy for the eye.
tavrelk tavrelk
Update: I have decided to add an additional winner. I will pick two designs that include business card and stationary. Thanks for the submissions. Also, designers, I am launching a website design contest soon. Keep an eye out for that.
Mistake in Brief. Please use phone number 217-555-0176 when submitting designs. Thank you.

```html
<!DOCTYPE html>
<html lang="en">
<head>
<meta charset="utf-8">
<title>Dunmore Law Office – Stationery Set</title>
<link href="https://fonts.googleapis.com/css2?family=Montserrat:wght@700&family=Open+Sans:wght@400;600&display=swap" rel="stylesheet">
<style>
  :root{
    --brand-blue:#1c6e97;
    --brand-blue-dark:#155a7d;
    --swoosh-grey:#c9ced3;
    --paper:#ffffff;
    --backdrop:#e4e6e8;
    --ink:#5a5f64;
    --ink-light:#8d9297;
  }
  *{box-sizing:border-box;margin:0;padding:0}
  html,body{width:1200px;height:937px;overflow:hidden;background:var(--backdrop)}
  body{position:relative;font-family:"Open Sans",Arial,sans-serif;color:var(--ink)}
  .sheet{position:absolute;background:var(--paper);box-shadow:0 2px 8px rgba(0,0,0,.18);overflow:hidden}
  .footer-wave{position:absolute;left:0;bottom:0;width:100%}
  .web{position:absolute;left:0;width:100%;text-align:center;color:#fff;font-size:10px;letter-spacing:2px;font-weight:600}

  .brand{display:flex;align-items:center;gap:.4em;color:var(--brand-blue);font-family:"Montserrat",Arial,sans-serif;font-weight:700;text-transform:uppercase;white-space:nowrap}
  .brand-dot{width:1.1em;height:1.1em;border-radius:50%;background:var(--brand-blue);flex:none}
  .brand.stacked{flex-direction:column;gap:.35em;text-align:center}
  .brand.stacked .brand-dot{width:2.4em;height:2.4em}
  .brand.on-blue{color:#fff}
  .brand.on-blue .brand-dot{background:#fff}

  /* letterhead */
  .letterhead{left:114px;top:56px;width:456px;height:564px}
  .letterhead .brand{position:absolute;left:58px;top:38px;font-size:15px}
  .lh-contact{position:absolute;right:34px;top:34px;text-align:right;font-size:5.5px;line-height:9px;color:var(--ink-light)}
  .letter-body{position:absolute;left:58px;top:135px;width:340px;font-size:5.6px;line-height:9px;color:var(--ink)}
  .letter-body p{margin-bottom:9px}
  .signature{width:34px;height:16px;margin:4px 0 6px;background:linear-gradient(90deg,#6b7075,#9aa0a5);border-radius:8px;opacity:.5}
  .letterhead .web{bottom:8px;font-size:8px}

  /* folder */
  .folder{left:633px;top:56px;width:460px;height:564px}
  .folder .brand{position:absolute;left:0;right:0;top:190px;justify-content:center;font-size:24px}
  .folder .web{bottom:8px;font-size:8px}

  /* business cards */
  .card{width:202px;height:104px;border-radius:3px}
  .card-front{left:46px;top:663px}
  .card-front .brand{position:absolute;left:12px;top:22px;font-size:8px}
  .card-contact{position:absolute;left:108px;top:20px;font-size:4.6px;line-height:8px;color:var(--ink-light)}
  .card-contact strong{color:var(--ink);font-weight:600;font-size:5.4px}
  .card-front .web{bottom:3px;font-size:4.5px;letter-spacing:1px}
  .card-back{left:46px;top:780px;background:var(--brand-blue);border-radius:6px}
  .card-back .brand{position:absolute;left:14px;top:44px;font-size:9px}

  /* envelopes */
  .envelope{width:430px;height:223px}
  .envelope-front{left:266px;top:663px}
  .envelope-front .brand{position:absolute;left:30px;top:34px;font-size:13px}
  .envelope-front .web{bottom:6px;font-size:7px}
  .envelope-back{left:734px;top:663px}
  .envelope-back .web{top:22px;font-size:8px}
</style>
</head>
<body>

<section class="sheet letterhead" aria-label="Letterhead">
  <div class="brand"><span class="brand-dot"></span>Dunmore Law Office</div>
  <address class="lh-contact" style="font-style:normal">
    217-555-0143<br>217-555-0176<br>ray@dunmorelawoffice.example<br>dunmorelawoffice.example
  </address>
  <div class="letter-body">
    <p>June 4, 2024<br><br>Mr. Alan Porter<br>1200 Harbor Rd, Suite 4</p>
    <p>Thank you for meeting with our office this week. We have reviewed the documents you provided and prepared a short summary of the next steps in your case. Please read it carefully and call us with any questions.</p>
    <p>Our team will contact the court on your behalf and confirm the hearing date. We will send you copies of every filing as soon as they are made.</p>
    <p>If anything changes before then, please let us know right away so we can adjust our plan and protect your interests at every stage.</p>
    <p>Sincerely,</p>
    <div class="signature" role="img" aria-label="Handwritten signature"></div>
    <p>Ray Dunmore<br>Attorney<br>418 N Willowbend Ave Lincoln, IL 62871</p>
  </div>
  <svg class="footer-wave" viewBox="0 0 456 70" height="70" preserveAspectRatio="none" aria-hidden="true">
    <path d="M0 40 Q228 -5 456 30 L456 36 Q228 4 0 48 Z" fill="var(--swoosh-grey)"/>
    <path d="M0 50 Q228 6 456 36 L456 70 L0 70 Z" fill="var(--brand-blue)"/>
  </svg>
  <div class="web">www.DunmoreLawOffice.example</div>
</section>

<section class="sheet folder" aria-label="Presentation folder">
  <div class="brand stacked"><span class="brand-dot"></span>Dunmore<br>Law Office</div>
  <svg class="footer-wave" viewBox="0 0 460 70" height="70" preserveAspectRatio="none" aria-hidden="true">
    <path d="M0 40 Q230 -5 460 30 L460 36 Q230 4 0 48 Z" fill="var(--swoosh-grey)"/>
    <path d="M0 50 Q230 6 460 36 L460 70 L0 70 Z" fill="var(--brand-blue)"/>
  </svg>
  <div class="web">www.DunmoreLawOffice.example</div>
</section>

<section class="sheet card card-front" aria-label="Business card, contact side">
  <div class="brand stacked"><span class="brand-dot"></span>Dunmore<br>Law Office</div>
  <div class="card-contact">
    <strong>Ray Dunmore</strong><br>Attorney at Law<br>P: 217-555-0176<br>E: ray@dunmorelawoffice.example<br>W: DunmoreLawOffice.example
  </div>
  <svg class="footer-wave" viewBox="0 0 202 22" height="22" preserveAspectRatio="none" aria-hidden="true">
    <path d="M0 12 Q101 -2 202 8 L202 11 Q101 1 0 15 Z" fill="var(--swoosh-grey)"/>
    <path d="M0 16 Q101 2 202 11 L202 22 L0 22 Z" fill="var(--brand-blue)"/>
  </svg>
  <div class="web">www.DunmoreLawOffice.example</div>
</section>

<section class="sheet card card-back" aria-label="Business card, brand side">
  <div class="brand on-blue"><span class="brand-dot"></span>Dunmore Law Office</div>
</section>

<section class="sheet envelope envelope-front" aria-label="Envelope front">
  <div class="brand stacked"><span class="brand-dot"></span>Dunmore<br>Law Office</div>
  <svg class="footer-wave" viewBox="0 0 430 50" height="50" preserveAspectRatio="none" aria-hidden="true">
    <path d="M0 26 Q215 -4 430 20 L430 25 Q215 3 0 32 Z" fill="var(--swoosh-grey)"/>
    <path d="M0 34 Q215 4 430 25 L430 50 L0 50 Z" fill="var(--brand-blue)"/>
  </svg>
  <div class="web">www.DunmoreLawOffice.example</div>
</section>

<section class="sheet envelope envelope-back" aria-label="Envelope back">
  <svg viewBox="0 0 430 223" width="430" height="223" preserveAspectRatio="none" aria-hidden="true">
    <path d="M0 0 L430 0 L430 86 Q215 130 0 86 Z" fill="var(--brand-blue)"/>
    <path d="M0 86 Q215 130 430 86 L430 92 Q215 138 0 92 Z" fill="var(--swoosh-grey)"/>
  </svg>
  <div class="web">www.DunmoreLawOffice.example</div>
</section>

</body>
</html>
```